Veterinary Clinic Letterhead - Ridgeline Veterinary Surgery

We need a letterhead design for an established Veterinary Clinic in Mareeba called Ridgeline Veterinary Surgery. We are a moderate sized mixed animal veterinary clinic offering a wide variety of veterinary services. The design should use the same colour pattern as those in the logos supplied. The design should also include our address (58 Corvane Street, Tallowbrook, Queensland, 4899), phone number (07 4167 5830), email (admin@ridgelinevets.example.au), website (www.ridgelinevets.example.au) and our opening hours (8am to 5pm Monday to Friday and 8am to 12pm Saturday).
Target Market(s)
Pet owners
Industry/Entity Type
Veterinary
Requirements
Must have
- The logo or modification of it, business address, opening hours, website, phone number and email address

```html
<!DOCTYPE html>
<html lang="en">
<head>
<meta charset="utf-8">
<title>Ridgeline Veterinary Surgery – Letterhead</title>
<link href="https://fonts.googleapis.com/css2?family=Lato:wght@400;700&family=Montserrat:wght@500&family=Tangerine:wght@400;700&display=swap" rel="stylesheet">
<style>
  :root {
    --navy: #0f2d52;
    --ink: #2a2a2a;
    --paper: #ffffff;
    --backdrop: #e6e7e9;
  }
  * { box-sizing: border-box; margin: 0; padding: 0; }
  html, body { width: 1200px; height: 1200px; overflow: hidden; background: var(--backdrop); }
  .letterhead {
    position: absolute; left: 214px; top: 40px; width: 771px; height: 1120px;
    background: var(--paper); overflow: hidden;
    font-family: "Lato", Arial, sans-serif; color: var(--ink);
    box-shadow: 0 6px 24px rgba(0,0,0,0.18);
  }
  .brand { position: absolute; left: 38px; top: 38px; width: 250px; text-align: center; }
  .brand-mark { display: block; width: 116px; height: 116px; margin: 0 auto 14px; border-radius: 50%; background: var(--navy); }
  .brand-name {
    font-family: "Montserrat", Arial, sans-serif; font-weight: 500; color: var(--navy);
    font-size: 19px; letter-spacing: 0.4px; line-height: 1.1; text-transform: uppercase;
    white-space: nowrap;
  }
  .brand-sub {
    display: flex; align-items: center; gap: 8px; margin-top: 3px;
    font-family: "Montserrat", Arial, sans-serif; font-weight: 500; color: var(--navy);
    font-size: 11px; letter-spacing: 4px; text-transform: uppercase;
  }
  .brand-sub::before, .brand-sub::after { content: ""; flex: 1; height: 1.5px; background: var(--navy); }
  .contact {
    position: absolute; left: 556px; top: 41px; height: 90px;
    border-left: 1.5px solid var(--navy); padding-left: 12px;
    font-size: 11.5px; color: #1b1b1b; line-height: 17px; font-style: normal;
  }
  .contact .address { margin-bottom: 5px; }
  .contact .address span { display: block; }
  .contact .address span + span { padding-left: 4px; }
  .contact-row { display: flex; align-items: center; gap: 6px; }
  .contact-row svg { width: 10px; height: 10px; flex: none; }
  .icon-fill { fill: var(--navy); }
  .icon-line { fill: none; stroke: var(--navy); stroke-width: 2.4; }
  .letter { position: absolute; left: 50px; top: 284px; width: 684px; font-size: 15px; line-height: 17.8px; }
  .date { font-size: 16px; margin-bottom: 20px; }
  .recipient { font-size: 15px; line-height: 18.5px; margin-bottom: 18px; }
  .salutation { font-size: 19px; font-weight: 700; margin: 22px 0 14px; color: #1d1d1d; }
  .letter p.body { text-align: justify; margin-bottom: 17px; }
  .closing { margin-top: 40px; font-size: 14.5px; }
  .signature { font-family: "Tangerine", cursive; font-weight: 700; font-size: 48px; line-height: 1; margin-top: 22px; color: #111; }
  .hours { position: absolute; left: 0; right: 0; top: 1024px; text-align: center; font-size: 12px; line-height: 17px; color: #111; }
  .footer-bands { position: absolute; left: 0; bottom: 0; width: 771px; height: 52px; }
  .footer-bands polygon { fill: var(--navy); }
</style>
</head>
<body>
  <main class="letterhead">
    <header>
      <div class="brand">
        <span class="brand-mark" aria-hidden="true"></span>
        <div class="brand-name">Ridgeline Veterinary</div>
        <div class="brand-sub">Surgery</div>
      </div>
      <address class="contact">
        <div class="address"><span>58 Corvane Street,</span><span>Tallowbrook,Queensland, 4899</span></div>
        <div class="contact-row">
          <svg viewBox="0 0 24 24"><path class="icon-fill" d="M6.6 10.8a15 15 0 0 0 6.6 6.6l2.2-2.2c.3-.3.7-.4 1-.2 1.1.4 2.3.6 3.6.6.6 0 1 .4 1 1V20c0 .6-.4 1-1 1C10.6 21 3 13.4 3 4c0-.6.4-1 1-1h3.5c.6 0 1 .4 1 1 0 1.3.2 2.5.6 3.6.1.3 0 .7-.2 1z"/></svg>
          <span>07 4167 5830</span>
        </div>
        <div class="contact-row">
          <svg viewBox="0 0 24 24"><rect class="icon-fill" x="2" y="5" width="20" height="14" rx="1"/><path d="M3 6l9 7 9-7" fill="none" stroke="#fff" stroke-width="2"/></svg>
          <span>admin@ridgelinevets.example.au</span>
        </div>
        <div class="contact-row">
          <svg viewBox="0 0 24 24"><circle class="icon-line" cx="12" cy="12" r="9.5"/><ellipse class="icon-line" cx="12" cy="12" rx="4" ry="9.5"/><path class="icon-line" d="M2.5 12h19"/></svg>
          <span>www.ridgelinevets.example.au</span>
        </div>
      </address>
    </header>

    <section class="letter">
      <p class="date">January-03-2020</p>
      <p class="recipient">Mr, Owen Pryce<br>President</p>
      <p class="recipient">Harlow Corporation<br>123 Street Name, Suite# 10<br>City, State, 120023</p>
      <p class="salutation">Dear Mr, Owen</p>
      <p class="body">Lorem ipsum dolor sit amet, consectetur adipisicing elit, sed do eiusmod tempor incididunt ut labore et dolore magna aliqua. Ut enim ad minim veniam, quis nostrud exercitation ullamco laboris nisi ut aliquip ex ea commodo consequat. Duis aute irure dolor in reprehenderit in voluptate velit esse cillum dolore eu fugiat nulla pariatur.</p>
      <p class="body">Lorem ipsum dolor sit amet, consectetur adipisicing elit, sed do eiusmod tempor incididunt ut labore et dolore magna aliqua. Ut enim ad minim veniam, quis nostrud exercitation ullamco laboris nisi ut aliquip ex ea commodo consequat. Duis aute irure dolor in reprehenderit in voluptate velit esse cillum dolore eu fugiat nulla pariatur.</p>
      <p class="body">Lorem ipsum dolor sit amet, consectetur adipisicing elit, sed do eiusmod tempor incididunt ut labore et dolore magna aliqua. Ut enim ad minim veniam, quis nostrud exercitation ullamco laboris nisi ut aliquip ex ea commodo consequat.</p>
      <p class="body">Excepteur sint occaecat cupidatat non proident, sunt in culpa qui officia deserunt mollit anim id est laborum. re et dolore magnam aliquam quaerat voluptatem.</p>
      <p class="closing">Regards</p>
      <p class="signature">Daniel Hart</p>
    </section>

    <footer>
      <p class="hours">our opening hours<br>8am to 5pm Monday to Friday and 8am to 12pm Saturday</p>
      <svg class="footer-bands" viewBox="0 1068 771 52" aria-hidden="true">
        <polygon points="0,1078 432,1078 426,1084 0,1084"/>
        <polygon points="0,1094 416,1094 390,1120 0,1120"/>
        <polygon points="456,1068 771,1068 771,1120 404,1120"/>
      </svg>
    </footer>
  </main>
</body>
</html>
```